Quillon Maison Wood Fired Pizza business card design

I have a logo and need an eye catching design that will get me noticed.
My business is wood fired pizza. I want a bold design that will make our customers remember us and the food that we serve. Work with the colors of our logo and texts. Maybe add designs that lend to what or how pizza is made using our wood fired oven?

Target Market(s)

Foodies!

Contact Information for Business Card

Quillon Maison Wood Fired Pizza
Our slogan is Fast. Fresh. Handcrafted
Catering for all events

Requirements
Must have
• Dana Porrick
Telephone 570 555 0183
website www.getquillon.example
Facebook @getquillonpizza maybe use the facebook logo next to it
Instagram getquillonpizza maybe use the instagram logo next to it
Catering for all events
Nice to have
• Maybe pizza peels, pizza cutters? Wood? Fired wood? Using our flame in the background?
Please work with different colored text so each sentence stands out? A themed color for facebook?
Maybe work with the colors within our logo?
Please try to use the our quillon font, but not a must have.

```html
<!DOCTYPE html>
<html lang="en">
<head>
<meta charset="utf-8">
<title>Quillon Maison Wood Fired Pizza – Business Card</title>
<link rel="stylesheet" href="https://fonts.googleapis.com/css2?family=Oswald:wght@600;700&family=Barlow:wght@400;600&display=swap">
<style>
  :root {
    --backdrop: #e4e4e4;
    --card: #13161d;
    --ember-red: #c42026;
    --flame-orange: #f0901e;
    --ash-white: #f3f1ee;
    --text-soft: #e6e6e6;
  }
  * { margin: 0; padding: 0; box-sizing: border-box; }
  html, body {
    width: 1200px; height: 960px; overflow: hidden;
    background: var(--backdrop);
  }
  .stage { position: relative; width: 1200px; height: 960px; }
  .card {
    position: absolute; left: 324px; width: 556px; height: 318px;
    background: var(--card); overflow: hidden;
  }
  .card-front { top: 137px; }
  .card-back { top: 505px; }

  /* Front */
  .brand-dot {
    position: absolute; left: 208px; top: 34px;
    width: 140px; height: 140px; border-radius: 50%;
    background: var(--ember-red);
  }
  .hearth-line {
    position: absolute; left: 196px; top: 189px; width: 164px; height: 8px;
  }
  .brand {
    position: absolute; left: 0; right: 0; top: 212px;
    text-align: center; color: var(--ash-white);
    font-family: "Oswald", sans-serif; font-weight: 700; text-transform: uppercase;
  }
  .brand-tagline {
    display: block; font-size: 14px; line-height: 16px; letter-spacing: 1.4px;
  }
  .brand-name {
    display: block; margin-top: 2px;
    font-size: 50px; line-height: 54px; letter-spacing: 7px; padding-left: 7px;
  }
  .est-row {
    position: absolute; left: 176px; top: 278px; width: 220px; height: 20px;
  }
  .est-label {
    position: absolute; left: 0; right: 0; top: 279px; text-align: center;
    font-family: "Oswald", sans-serif; font-weight: 700; font-size: 7px;
    letter-spacing: 0.6px; color: var(--ash-white);
  }

  /* Back */
  .holder {
    position: absolute; left: 54px; top: 60px;
    font-family: "Oswald", sans-serif; font-weight: 700;
    font-size: 25px; line-height: 1; letter-spacing: 0.3px; text-transform: uppercase;
  }
  .holder-first { color: var(--ember-red); }
  .holder-last { color: var(--flame-orange); }

  .contact-list {
    position: absolute; left: 53px; top: 127px; list-style: none;
    font-family: "Barlow", sans-serif; font-size: 14px; color: var(--text-soft);
  }
  .contact-list li { display: flex; align-items: center; gap: 6px; height: 18.7px; }
  .contact-icon { width: 13px; height: 13px; flex: none; }
  .contact-dot {
    width: 11px; height: 11px; margin: 0 1px; border-radius: 50%;
    background: var(--flame-orange); flex: none;
  }

  .service {
    position: absolute; left: 53px; top: 216px;
    font-family: "Barlow", sans-serif; font-size: 14px; color: var(--text-soft);
  }
  .slogan {
    position: absolute; left: 53px; top: 263px;
    font-family: "Barlow", sans-serif; font-weight: 600; font-size: 14px;
    text-transform: uppercase;
  }
  .slogan-fast, .slogan-crafted { color: var(--flame-orange); }
  .slogan-fresh { color: var(--ember-red); }

  .ember-disc {
    position: absolute; left: 318px; top: 36px;
    width: 240px; height: 240px; border-radius: 50%;
    background: var(--ember-red);
  }
  .peel-streak {
    position: absolute; right: 0; top: 286px; width: 284px; height: 10px;
  }
</style>
</head>
<body>
<main class="stage">
  <section class="card card-front" aria-label="Card front">
    <span class="brand-dot" aria-hidden="true"></span>
    <svg class="hearth-line" viewBox="0 0 164 8" preserveAspectRatio="none" aria-hidden="true">
      <path d="M0 4 Q82 -1 164 4 Q82 9 0 4 Z" fill="#f0901e"/>
    </svg>
    <h2 class="brand">
      <span class="brand-tagline">Maison Wood Fired Pizza</span>
      <span class="brand-name">Quillon</span>
    </h2>
    <svg class="est-row" viewBox="0 0 220 20" aria-hidden="true">
      <path d="M0 17 Q40 8 88 6 L88 8 Q40 10 0 17 Z" fill="#f0901e"/>
      <path d="M220 17 Q180 8 132 6 L132 8 Q180 10 220 17 Z" fill="#f0901e"/>
    </svg>
    <span class="est-label">EST. 2020</span>
  </section>

  <section class="card card-back" aria-label="Card back">
    <h1 class="holder"><span class="holder-first">Dana</span> <span class="holder-last">Porrick</span></h1>

    <ul class="contact-list">
      <li>
        <svg class="contact-icon" viewBox="0 0 24 24" aria-hidden="true"><path fill="#f0901e" d="M6.6 10.8a15.2 15.2 0 0 0 6.6 6.6l2.2-2.2c.3-.3.7-.4 1-.2 1.1.4 2.3.6 3.6.6.6 0 1 .4 1 1V20c0 .6-.4 1-1 1A17 17 0 0 1 3 4c0-.6.4-1 1-1h3.5c.6 0 1 .4 1 1 0 1.3.2 2.5.6 3.6.1.3 0 .7-.2 1l-2.3 2.2z"/></svg>
        570 555 0183
      </li>
      <li>
        <svg class="contact-icon" viewBox="0 0 24 24" aria-hidden="true"><g fill="none" stroke="#f0901e" stroke-width="2"><circle cx="12" cy="12" r="10"/><ellipse cx="12" cy="12" rx="4.5" ry="10"/><path d="M2 12h20M4 6.5h16M4 17.5h16"/></g></svg>
        www.getquillon.example
      </li>
      <li><span class="contact-dot" aria-hidden="true"></span>@getquillonpizza</li>
      <li><span class="contact-dot" aria-hidden="true"></span>getquillonpizza</li>
    </ul>

    <p class="service">Catering for all events</p>

    <p class="slogan"><span class="slogan-fast">Fast.</span> <span class="slogan-fresh">Fresh.</span> <span class="slogan-crafted">Handcrafted</span></p>

    <span class="ember-disc" aria-hidden="true"></span>
    <svg class="peel-streak" viewBox="0 0 284 10" preserveAspectRatio="none" aria-hidden="true">
      <path d="M0 5 Q142 0 284 1 L284 9 Q142 10 0 5 Z" fill="#f0901e"/>
    </svg>
  </section>
</main>
</body>
</html>
```